The Wellness Barn Business Card

Info for the front..... (in whichever order and layout looks best)
Carla Penhallow
Physiotherapist
4/37 Upper Creekbank Rd
Tallowbrook
QLD 4712
0462305178
carlapenhallow57@mailbox.example
www.thewellnessbarn.example.au
on the back I would like to be able to write appointments so probably just that heading with lines.
I like a sort of rustic style but mostly professional, colours in naturals, beige, brown, green etc. I dont mind if the logo colour is changed slightly to suit.

```html
<!DOCTYPE html>
<html lang="en">
<head>
<meta charset="utf-8">
<title>The Wellness Barn – Business Card</title>
<link href="https://fonts.googleapis.com/css2?family=Montserrat:wght@400;500;700;800&display=swap" rel="stylesheet">
<style>
  :root {
    --green: #3a4828;
    --green-line: #4d5c38;
    --white: #ffffff;
    --ink-soft: #6f6f6f;
    --backdrop: #cfcfcf;
  }
  * { box-sizing: border-box; margin: 0; padding: 0; }
  html, body { width: 1200px; height: 802px; overflow: hidden; }
  body {
    background: var(--backdrop);
    font-family: "Montserrat", sans-serif;
    position: relative;
  }
  .card {
    position: absolute;
    top: 243px;
    width: 520px;
    height: 316px;
    border-radius: 22px;
    overflow: hidden;
    box-shadow: 0 10px 24px rgba(0,0,0,0.18);
  }
  /* Front */
  .card-front { left: 60px; background: var(--white); }
  .front-wave { position: absolute; inset: 0; width: 100%; height: 100%; }
  .brand-name {
    position: absolute;
    font-weight: 800;
    line-height: 1.02;
    letter-spacing: 0.5px;
  }
  .card-front .brand-name { left: 36px; top: 36px; font-size: 26px; color: var(--green); }
  .name-block { position: absolute; right: 58px; top: 42px; text-align: right; }
  .person-name { font-weight: 700; font-size: 19px; color: var(--green); letter-spacing: 0.6px; }
  .person-role { font-size: 12.5px; color: var(--ink-soft); margin-top: 3px; letter-spacing: 0.4px; }
  .corner-square {
    position: absolute; right: 0; top: 40px;
    width: 22px; height: 36px; background: var(--green);
  }
  .contact-list {
    position: absolute; left: 36px; top: 134px;
    font-size: 12.5px; color: var(--ink-soft); line-height: 18px; list-style: none;
  }
  .contact-list li { display: flex; align-items: center; gap: 7px; }
  .contact-list svg { width: 11px; height: 11px; flex: none; }
  .website {
    position: absolute; right: 30px; bottom: 18px;
    display: flex; align-items: center; gap: 6px;
    font-size: 12.5px; color: var(--white); letter-spacing: 0.3px;
  }
  .website svg { width: 11px; height: 11px; }
  /* Back */
  .card-back { left: 620px; background: var(--green); color: var(--white); }
  .card-back .brand-name {
    left: 0; right: 0; top: 46px; text-align: center;
    font-size: 32px; color: var(--white);
  }
  .appointment-lines { position: absolute; left: 38px; right: 38px; top: 170px; }
  .line-row { display: flex; align-items: flex-end; gap: 10px; font-size: 14px; margin-bottom: 26px; }
  .line-row .label { white-space: nowrap; letter-spacing: 0.4px; }
  .line-row .fill { flex: 1; border-bottom: 1.5px dotted rgba(255,255,255,0.75); height: 14px; }
  .line-row .suffix { white-space: nowrap; }
</style>
</head>
<body>

<section class="card card-front" aria-label="Business card front">
  <svg class="front-wave" viewBox="0 0 520 316" preserveAspectRatio="none" aria-hidden="true">
    <path d="M0 296 C 180 305, 330 270, 400 210 C 440 175, 480 158, 520 155 L520 316 L0 316 Z" fill="var(--green)"/>
    <path d="M0 284 C 180 293, 325 258, 395 198 C 435 163, 478 146, 520 143" fill="none" stroke="var(--green-line)" stroke-width="1.5"/>
  </svg>
  <div class="brand-name">The<br>Wellness<br>Barn</div>
  <div class="corner-square"></div>
  <div class="name-block">
    <div class="person-name">CARLA PENHALLOW</div>
    <div class="person-role">Physiotherapist</div>
  </div>
  <ul class="contact-list">
    <li>4/37 Upper Creekbank Rd</li>
    <li>Tallowbrook QLD 4712</li>
    <li><svg viewBox="0 0 12 12"><rect x="3" y="0.5" width="6" height="11" rx="1.2" fill="none" stroke="var(--green)" stroke-width="1.3"/></svg>0462305178</li>
    <li><svg viewBox="0 0 12 12"><rect x="0.5" y="2" width="11" height="8" fill="var(--green)"/><path d="M0.5 2 L6 7 L11.5 2" fill="none" stroke="#fff" stroke-width="1"/></svg>carlapenhallow57@mailbox.example</li>
  </ul>
  <div class="website">
    <svg viewBox="0 0 12 12"><circle cx="6" cy="6" r="5.5" fill="var(--white)"/><path d="M1 6 H11 M6 1 C3 4,3 8,6 11 C9 8,9 4,6 1" fill="none" stroke="var(--green)" stroke-width="0.9"/></svg>
    www.thewellnessbarn.example.au
  </div>
</section>

<section class="card card-back" aria-label="Business card back">
  <div class="brand-name">The Wellness Barn</div>
  <div class="appointment-lines">
    <div class="line-row"><span class="fill"></span></div>
    <div class="line-row"><span class="label">Name :</span><span class="fill"></span><span class="label">Time :</span><span class="fill"></span><span class="suffix">am/pm</span></div>
    <div class="line-row"><span class="label">Date :</span><span class="fill"></span></div>
  </div>
</section>

</body>
</html>
```